Halden Pelvic Care Clinics needs promo/informational brochure for marketing

Our practice has added a new practitioner and our goal is to highlight her (Nell Brisco, PA-C) in this marketing campaign while providing useful information about the practice and conditions we treat. We have also closed our Maryland Office and moved to a new NY office (7 E. 81st St. Suite 512 NY, NY 10028). I have included a copy of what our last brochure looked like as an example of what I absolutely despise:) We are removing Loretta Quince from the brochure and adding a book (also attached). We want something modern, concise, streamlined, and professional. We would love to see what you all can come up with! The sooner we get responses, the better!

Target Market(s)

physicians and patients

Industry/Entity Type

Medical

Font styles to use
Other font styles liked:
• avenir book? i'll leave it to the designer!

Colors
ffffff
cee9f5
e4daeb
000000
9d9d9d
cbcbcb

Requirements
Must have
• some sort of lotus image....or some type of background from stock images
• This is the bio of Nell Brisco to be included:
• Nell Brisco, PA
• Nell Brisco is a Nationally Certified Physician Assistant licensed in New York and Washington, DC. She graduated with honors from Wexley College of Health Sciences where she was awarded the prestigious Pemberton Award.
• Nell has been treating women with sexual dysfunction since 2010. She has extensive experience treating vaginismus, vulvodynia and other vulvovaginal disorders. She also has expertise in treating hypoactive sexual desire (low libido), arousal, and orgasmic disorders. Nell has lectured and written extensively on the topic of female sexual dysfunction and is a member of the Global Council for Research on Female Intimate Wellness.
• Nell practiced as a PA in psychiatry and orthopedic surgery before she became a female sexual medicine specialist. She is also a member of the Families of Overseas Servicemen Care Network and has volunteered in Vietnam providing medical care with Youth Hope Outreach Global (YHOG). Nell also studied at Carrow University in Australia and she spent two years living in Japan where she taught English with the Overseas Language Assistant Scheme.

```html
<!DOCTYPE html>
<html lang="en">
<head>
<meta charset="utf-8">
<title>Halden Pelvic Care Clinics – Brochure</title>
<link href="https://fonts.googleapis.com/css2?family=Questrial&family=Didact+Gothic&display=swap" rel="stylesheet">
<style>
:root{
  --white:#ffffff;
  --sky:#cee9f5;
  --lilac:#e4daeb;
  --ink:#000000;
  --grey:#9d9d9d;
  --silver:#cbcbcb;
  --text:#2b2b2b;
  --muted:#6f6f6f;
}
*{box-sizing:border-box;margin:0;padding:0}
html,body{width:1200px;height:1200px;overflow:hidden}
body{background:var(--silver);font-family:"Didact Gothic",sans-serif;color:var(--text);position:relative}
.spread{position:absolute;left:40px;width:1120px;height:575px;display:grid;grid-template-columns:repeat(3,1fr);grid-template-rows:1fr 34px;overflow:hidden;
  background:linear-gradient(170deg,var(--white) 0%,var(--white) 45%,var(--lilac) 100%);
  box-shadow:0 2px 10px rgba(0,0,0,.12)}
.spread.outside{top:16px}
.spread.inside{top:609px}
.panel{padding:24px 24px 14px;position:relative;overflow:hidden}
.panel + .panel{border-left:1px solid var(--lilac)}
.footer{background:var(--ink);display:flex;align-items:center;justify-content:center;font-family:"Questrial",sans-serif;color:var(--white);font-size:15px;letter-spacing:.4px}
h2{font-family:"Questrial",sans-serif;font-weight:400;font-size:22px;color:var(--ink);letter-spacing:.5px;text-transform:uppercase;margin-bottom:16px;position:relative}
h2 .accent{color:var(--grey)}
h3{font-family:"Questrial",sans-serif;font-weight:400;font-size:13px;color:var(--ink);text-transform:uppercase;letter-spacing:.4px;margin-bottom:5px;padding-bottom:4px;border-bottom:2px solid var(--sky);display:inline-block}
p{font-size:10px;line-height:1.5;position:relative}
.lotus{position:absolute;border-radius:50%;background:radial-gradient(ellipse at 50% 55%,var(--lilac) 0%,var(--sky) 45%,rgba(206,233,245,0) 72%)}

/* locations */
.loc{margin-bottom:26px;position:relative}
.loc .note{font-size:9px;color:var(--muted);margin-top:5px}
.closing{position:absolute;left:24px;right:24px;bottom:18px;font-size:9.5px;color:var(--muted)}

/* books */
.book{display:flex;gap:12px;margin-bottom:10px;align-items:flex-start}
.cover{width:32px;height:46px;flex:none;border:1px solid var(--silver)}
.book p{font-size:8.6px;line-height:1.35;color:var(--muted)}
.book p strong{display:block;font-weight:400;font-family:"Questrial",sans-serif;font-size:10px;color:var(--ink)}
.book .new{color:var(--grey);font-size:8px;letter-spacing:.5px;text-transform:uppercase;margin-left:4px}

/* front */
.front{text-align:center;background:linear-gradient(180deg,var(--sky) 0%,var(--white) 60%)}
.title{font-family:"Questrial",sans-serif;font-size:25px;line-height:1.2;color:var(--ink);text-transform:uppercase;letter-spacing:.6px;margin-top:6px}
.cities{font-size:10px;color:var(--muted);letter-spacing:1px;margin:8px 0 16px;text-transform:uppercase}
.hero{height:190px;margin:0 10px;border-radius:4px;background:radial-gradient(ellipse at 50% 70%,var(--lilac) 0%,var(--sky) 55%,var(--white) 100%)}
.cover-text{font-size:10px;color:var(--text);margin:16px 14px 0}
.address{position:absolute;left:0;right:0;bottom:18px;font-size:10px;line-height:1.5;color:var(--muted)}

/* treat */
.intro{font-size:9.6px;color:var(--muted);margin-bottom:12px}
.treat{list-style:none}
.treat li{font-size:10.6px;line-height:1.5;padding-left:14px;position:relative;color:var(--text)}
.treat li::before{content:"";position:absolute;left:0;top:5px;border-left:6px solid var(--grey);border-top:3.5px solid transparent;border-bottom:3.5px solid transparent}

/* philosophy */
.beliefs{list-style:none;position:relative}
.beliefs li{font-size:9.4px;line-height:1.5;padding-left:16px;position:relative;margin-bottom:11px}
.beliefs li::before{content:"";position:absolute;left:0;top:3px;width:7px;height:7px;background:var(--sky);border:1px solid var(--grey)}

/* who */
.bio{display:flex;gap:10px;margin-bottom:10px;align-items:flex-start}
.bio p{font-size:8.6px;line-height:1.42;flex:1}
.portrait{width:54px;height:54px;flex:none;border-radius:50%;border:2px solid var(--white);box-shadow:0 0 0 2px var(--sky);background:radial-gradient(circle at 50% 40%,var(--silver),var(--grey))}
.feature{background:var(--sky);padding:10px 12px 10px;border-radius:3px}
.feature-head{display:flex;gap:10px;align-items:center;margin-bottom:6px}
.feature-head .portrait{width:58px;height:58px}
.feature-name{font-family:"Questrial",sans-serif;font-size:14px;color:var(--ink);line-height:1.2}
.feature-name span{display:block;font-size:9px;color:var(--muted);letter-spacing:.8px;text-transform:uppercase}
.feature p{font-size:8.3px;line-height:1.4;margin-bottom:4px}
</style>
</head>
<body>

<section class="spread outside">
  <div class="panel locations">
    <div class="lotus" style="left:-40px;bottom:40px;width:260px;height:170px" role="img" aria-label="Soft lotus flower in the background"></div>
    <h2>Locations</h2>
    <div class="loc">
      <h3>Main Office</h3>
      <p>18 Alder Circle NW, Suite 310<br>Washington, DC 20036<br>Phone: (202) 555-0148<br>Fax: (202) 555-0172</p>
      <p class="note">Across the street from Riverside University Hospital and the Elm Park Metro</p>
    </div>
    <div class="loc">
      <h3>New York Office</h3>
      <p>7 E. 81st St. Suite 512<br>NY, NY 10028</p>
    </div>
    <p class="closing">Our office in Washington DC is our main office and all appointments and communications with both offices are made through this office.</p>
  </div>

  <div class="panel books">
    <h2>Our Books</h2>
    <div class="book"><div class="cover" style="background:var(--lilac)" role="img" aria-label="Book cover"></div><p><strong>When Intimacy Aches</strong>A guide for patients on more than twenty causes of sexual pain, with a clear path to the right treatment.</p></div>
    <div class="book"><div class="cover" style="background:var(--grey)" role="img" aria-label="Book cover"></div><p><strong>Pelvic Pain in Women</strong>The only textbook devoted to the diagnosis and treatment of pelvic pain disorders.</p></div>
    <div class="book"><div class="cover" style="background:var(--sky)" role="img" aria-label="Book cover"></div><p><strong>Renewing Desire</strong>Four keys to finding lost libido through a holistic approach to low desire.</p></div>
    <div class="book"><div class="cover" style="background:var(--white)" role="img" aria-label="Book cover"></div><p><strong>Answers on Vulvar Health</strong>Practical, trusted answers to common questions from women with vulvar conditions.</p></div>
    <div class="book"><div class="cover" style="background:var(--silver)" role="img" aria-label="Book cover"></div><p><strong>Care of Sexual Concerns in Adults</strong>A clear, authoritative guide to sexual function for patients and clinicians.</p></div>
    <div class="book"><div class="cover" style="background:var(--text)" role="img" aria-label="Book cover"></div><p><strong>Healing After Pain<span class="new">New</span></strong>Our newest title, a step-by-step guide to recovery from chronic vulvar pain.</p></div>
  </div>

  <div class="panel front">
    <div class="title">Halden Pelvic<br>Care Clinics</div>
    <div class="cities">Washington DC &nbsp;·&nbsp; New York City</div>
    <div class="hero" role="img" aria-label="Lotus flower in soft blue and lavender tones"></div>
    <p class="cover-text">For more than two decades, Halden Pelvic Care Clinics have been referral centers for the treatment of vulvodynia, sexual pain disorders, dermatologic diseases of the vulva, recurrent vulvovaginal infections, and female sexual dysfunction.</p>
    <p class="address">18 Alder Circle NW, Suite 310<br>Washington, DC 20036<br>Phone: (202) 555-0148</p>
  </div>

  <div class="footer">www.haldenpelvic.org</div>
  <div class="footer">www.haldenpelvic.org</div>
  <div class="footer">www.haldenpelvic.org</div>
</section>

<section class="spread inside">
  <div class="panel treat-panel">
    <h2>What We <span class="accent">Treat</span></h2>
    <p class="intro">The physicians of Halden Pelvic Care Clinics are experts in the diagnosis and treatment of more than two dozen diseases that cause the symptoms of genital itching, burning, irritation, rawness, throbbing, urinary frequency and urgency, and pain during sex. The diseases we treat include:</p>
    <ul class="treat">
      <li>Pain With Sex</li><li>Vaginal and Vulvar Discomfort</li><li>Burning, Rawness, Itching &amp; Pain</li><li>Vulvodynia</li><li>Vulvar Vestibulitis (Vestibulodynia)</li><li>Vulvovaginal Skin Diseases</li><li>Lichen Sclerosus</li><li>Lichen Planus</li><li>VIN</li><li>Lichen Simplex Chronicus</li><li>Plasma Cell Vulvitis</li><li>Pudendal Neuralgia</li><li>Chronic Pelvic Pain</li><li>Persistent Genital Arousal Disorder</li><li>Decreased Libido</li><li>Decreased Orgasm</li><li>Decreased Arousal</li><li>Pelvic Floor Muscle Dysfunction</li><li>Vaginismus</li><li>Interstitial Cystitis/Painful Bladder Syndrome</li>
    </ul>
  </div>

  <div class="panel philosophy">
    <div class="lotus" style="left:40px;bottom:-40px;width:300px;height:170px" role="img" aria-label="Soft lotus flower in the background"></div>
    <h2>Our Philosophy</h2>
    <ul class="beliefs">
      <li>It is our belief that quality medical care cannot be rushed. By taking a comprehensive medical history, we give our patients the opportunity to be heard.</li>
      <li>We pride ourselves on our precise physical examinations, diagnostic precision and effective treatment. With the use of specialized testing and extensive research, we have developed algorithms to achieve accuracy and specificity in our diagnoses and therapies.</li>
      <li>Patient education is critical to our treatment process. We ensure that our patients have their questions answered and are connected with reliable resources. As a result, our patients are given a sense of hope and empowerment.</li>
      <li>We believe in the importance of experience and expertise. It is imperative for us to stay current with the latest literature, to focus our attention exclusively on vulvovaginal disorders and to invest a great deal of our own time and resources on research. We conduct over a dozen medical studies each year to find new treatments for vulvovaginal diseases.</li>
      <li>In our effort to provide the best care possible, we employ a multidisciplinary approach to treatment. To accomplish this, we enlist the help of our colleagues in other arenas of sexual health care including physical therapists, sex therapists, psychologists, and nutritionists.</li>
    </ul>
  </div>

  <div class="panel who">
    <h2>Who We Are</h2>
    <div class="bio"><p>Dr. Owen Hartley has been the director of the clinics since 2002. He is the current President of the International Society for the Study of Vulvovaginal Health and a Fellow of IAVR, ACPC, and SRTA. He has published more than 75 abstracts, peer-reviewed articles, and book chapters.</p><div class="portrait" role="img" aria-label="Portrait of Dr. Owen Hartley"></div></div>
    <div class="bio"><p>Dr. Celia Marwood completed her Ob/Gyn residency at Marlow Medical and a fellowship in Female Pelvic Medicine and Reconstructive Surgery at the University of Brantley. She is an expert in female pelvic floor disorders and interstitial cystitis.</p><div class="portrait" role="img" aria-label="Portrait of Dr. Celia Marwood"></div></div>
    <div class="feature">
      <div class="feature-head"><div class="portrait" role="img" aria-label="Portrait of Nell Brisco, PA-C"></div><div class="feature-name">Nell Brisco, PA<span>Physician Assistant</span></div></div>
      <p>Nell Brisco is a Nationally Certified Physician Assistant licensed in New York and Washington, DC. She graduated with honors from Wexley College of Health Sciences where she was awarded the prestigious Pemberton Award.</p>
      <p>Nell has been treating women with sexual dysfunction since 2010. She has extensive experience treating vaginismus, vulvodynia and other vulvovaginal disorders. She also has expertise in treating hypoactive sexual desire (low libido), arousal, and orgasmic disorders. Nell has lectured and written extensively on the topic of female sexual dysfunction and is a member of the Global Council for Research on Female Intimate Wellness.</p>
      <p>Nell practiced as a PA in psychiatry and orthopedic surgery before she became a female sexual medicine specialist. She is also a member of the Families of Overseas Servicemen Care Network and has volunteered in Vietnam providing medical care with Youth Hope Outreach Global (YHOG). Nell also studied at Carrow University in Australia and spent two years living in Japan where she taught English with the Overseas Language Assistant Scheme.</p>
    </div>
  </div>

  <div class="footer">www.haldenpelvic.org</div>
  <div class="footer">www.haldenpelvic.org</div>
  <div class="footer">www.haldenpelvic.org</div>
</section>

</body>
</html>
```